Blue Heron IT Business Card - Clean, Simple

Need a simple, clean standard sized business card for an IT consulting business using existing logo and company colours. Background should be mainly white. Feel free to be creative but clean, simple, quiet design is preferred. Font is specified in logo but any sans serif fonts work.

Contact Information for card is as follows (doesn't need to be in this exact order):

Martin Calloway
Owner
martin@blueheronit.ca
705-391-2586
www.blueheronit.ca

Target Market(s)

Small to medium sized business.

Industry/Entity Type

IT Consulting

Contact Information for Business Card

Logo and contact info.

Font styles to use
Sans Serif

Colors
EE7325
F08F49
F5BC92
FAE3D3
FDF4ED

Requirements
Must have
• All white or mostly white background.

```html
<!DOCTYPE html>
<html lang="en">
<head>
<meta charset="utf-8">
<title>Blue Heron IT — Business Card</title>
<link rel="stylesheet" href="https://fonts.googleapis.com/css2?family=Montserrat:wght@700&family=Roboto:wght@400&display=swap">
<style>
  :root {
    --backdrop: #d2d5d6;
    --card: #fbfbfa;
    --ink: #151515;
    --ink-soft: #2e2e2e;
    --orange: #ee7325;
    --orange-deep: #d95a16;
    --rule: #9a9a9a;
  }
  * { box-sizing: border-box; margin: 0; padding: 0; }
  html, body {
    width: 1200px; height: 1050px; overflow: hidden;
    background: var(--backdrop);
  }
  .sheet {
    width: 1200px; height: 1050px;
    display: flex; flex-direction: column;
    align-items: center; justify-content: center; gap: 50px;
  }
  .card {
    position: relative;
    width: 770px; height: 440px;
    background: var(--card);
    border-bottom: 5px solid var(--orange-deep);
    box-shadow: 0 18px 40px rgba(0,0,0,0.18);
  }
  /* Wordmark */
  .wordmark {
    display: flex; align-items: center; gap: 14px;
    font-family: "Montserrat", sans-serif;
    font-weight: 700;
    color: var(--ink);
    letter-spacing: -0.5px;
    white-space: nowrap;
  }
  .wordmark-dot {
    flex: none; border-radius: 50%;
    background: var(--orange);
  }
  /* Front side */
  .card-front .brand {
    position: absolute; left: 0; top: 0;
    width: 330px; height: 100%;
    display: flex; align-items: center; justify-content: center;
  }
  .card-front .wordmark { font-size: 34px; }
  .card-front .wordmark-dot { width: 22px; height: 22px; }
  .divider {
    position: absolute; left: 336px; top: 110px;
    width: 1px; height: 220px;
    background: var(--rule);
  }
  .details {
    position: absolute; left: 380px; top: 112px;
    font-family: "Roboto", sans-serif;
  }
  .person-name {
    font-family: "Montserrat", sans-serif;
    font-weight: 700; font-size: 25px;
    color: var(--ink);
  }
  .person-role {
    font-size: 20px; color: var(--orange);
    margin-top: 2px;
  }
  .contact-list {
    list-style: none; margin-top: 46px;
    display: flex; flex-direction: column; gap: 8px;
  }
  .contact-item {
    display: flex; align-items: center; gap: 12px;
    font-size: 21px; color: var(--ink-soft);
  }
  .contact-icon {
    width: 20px; height: 20px; flex: none;
    stroke: var(--orange); fill: none; stroke-width: 1.6;
  }
  /* Back side */
  .card-back {
    display: flex; align-items: center; justify-content: center;
  }
  .card-back .wordmark { font-size: 52px; gap: 18px; }
  .card-back .wordmark-dot { width: 32px; height: 32px; }
</style>
</head>
<body>
<main class="sheet">
  <section class="card card-front" aria-label="Business card front">
    <div class="brand">
      <div class="wordmark"><span class="wordmark-dot"></span>Blue Heron IT</div>
    </div>
    <div class="divider"></div>
    <div class="details">
      <p class="person-name">Martin Calloway</p>
      <p class="person-role">Owner</p>
      <ul class="contact-list">
        <li class="contact-item">
          <svg class="contact-icon" viewBox="0 0 20 20" aria-hidden="true">
            <path d="M5 2.5 L8 2.5 L9 6.5 L7 8 Q8.5 11.5 12 13 L13.5 11 L17.5 12 L17.5 15 Q17.5 17.5 15 17.5 Q3 16.5 2.5 5 Q2.5 2.5 5 2.5 Z" fill="var(--orange)" stroke="none"/>
          </svg>
          705-391-2586
        </li>
        <li class="contact-item">
          <svg class="contact-icon" viewBox="0 0 20 20" aria-hidden="true">
            <rect x="2" y="4.5" width="16" height="11"/>
            <path d="M2 4.5 L10 11 L18 4.5"/>
          </svg>
          martin@blueheronit.ca
        </li>
        <li class="contact-item">
          <svg class="contact-icon" viewBox="0 0 20 20" aria-hidden="true">
            <circle cx="10" cy="10" r="8"/>
            <ellipse cx="10" cy="10" rx="3.5" ry="8"/>
            <path d="M2 10 H18 M3.5 6 H16.5 M3.5 14 H16.5"/>
          </svg>
          www.blueheronit.ca
        </li>
      </ul>
    </div>
  </section>

  <section class="card card-back" aria-label="Business card back">
    <div class="wordmark"><span class="wordmark-dot"></span>Blue Heron IT</div>
  </section>
</main>
</body>
</html>
```